New Coffee Brand Packaging Design

We need a package design for our new coffee brand called Brindle Oak Coffee. Our brand mission will be displayed on the packaging (along the side or the back) and we currently have a logo that should be displayed on the front. Feel free to suggest a new logo design as you are designing the packaging if it doesn't fit with your vision. The final design should be creative and conservative. We like coffee colors (dark and light browns, white, cream, black, gold). We also like chalkboard art imagery (i.e. coffee cups, theme words from our mission, people, etc.). One famous person from West Louisville, KY is Terrence Vogt (world famous boxer and activist). If there is a way to draw his image in more of an abstract way where it doesn't infringe any patents that would be the sort of creativity we would like in the packaging. Our coffee brand prides itself on being a coffee for the people. For the average joe, working American who enjoys a good cup of coffee and a good atmosphere.

Brindle Oak Coffee Mission: "We aim to be a coffee company for the people. The people who have an appreciation and love for family, community and who never forget where they came from. Our coffee was born out of West Louisville, KY…a place like many others where the hearts, the minds and the wills are strong. We hope you enjoy each and every cup. Peace & Blessings."

Requirements
Must have
• (On the side or on the back of the packaging) Brindle Oak Coffee Mission: "We aim to be a coffee company for the people. The people who have an appreciation and love for family, community and who never forget where they came from. Our coffee was born out of West Louisville, KY…a place like many others where the hearts, the minds and the wills are strong. We hope you enjoy each and every cup. Peace & Blessings."
Nice to have
• Coffee Colors: dark and light browns, white, cream, black, gold

```html
<!DOCTYPE html>
<html lang="en">
<head>
<meta charset="utf-8">
<title>Brindle Oak Coffee – Bag Design</title>
<link rel="stylesheet" href="https://fonts.googleapis.com/css2?family=Archivo+Black&family=Roboto+Condensed:wght@700&family=Roboto:wght@700;900&display=swap">
<style>
  :root {
    --backdrop: #1b1410;
    --kraft: #c9a477;
    --kraft-side: #b8925f;
    --kraft-edge: #a98453;
    --ink: #141210;
    --ink-soft: #2a2420;
    --stitch: #8a6a40;
  }
  * { margin: 0; padding: 0; box-sizing: border-box; }
  html, body { width: 1200px; height: 1200px; overflow: hidden; }
  body { background: var(--backdrop); position: relative; }

  .bag {
    position: absolute;
    left: 270px; top: 50px;
    width: 660px; height: 1100px;
    display: flex;
  }
  .bag__side {
    width: 120px; height: 100%;
    background: var(--kraft-side);
    border-right: 2px solid var(--kraft-edge);
    padding: 470px 10px 0 12px;
  }
  .mission {
    font-family: "Roboto Condensed", sans-serif;
    font-weight: 700;
    font-size: 12px;
    line-height: 1.4;
    text-transform: uppercase;
    color: var(--ink-soft);
  }

  .bag__front {
    position: relative;
    width: 540px; height: 100%;
    background: var(--kraft);
  }
  .stitch {
    position: absolute; left: 20px; right: 20px; top: 40px;
    border-top: 3px dotted var(--stitch);
  }
  .ribbon {
    position: absolute; left: 90px; top: 0;
    width: 230px; height: 420px;
  }
  .ribbon__label {
    position: absolute; left: 90px; top: 170px; width: 230px;
    text-align: center;
    font-family: "Roboto Condensed", sans-serif;
    font-weight: 700;
    color: var(--kraft);
    text-transform: uppercase;
    line-height: 1;
  }
  .ribbon__label .small { display: block; font-size: 34px; }
  .ribbon__label .big { display: block; font-size: 50px; margin-top: 4px; }

  .brand {
    position: absolute; left: 0; right: 0; top: 470px;
    text-align: center;
  }
  .brand__dot {
    display: block; width: 70px; height: 70px;
    margin: 0 auto 24px;
    border: 6px solid var(--ink); border-radius: 50%;
  }
  .brand__name {
    font-family: "Archivo Black", sans-serif;
    font-size: 78px; line-height: 0.98;
    color: var(--ink);
    text-transform: uppercase;
  }
  .brand__tag {
    margin-top: 26px;
    font-family: "Roboto", sans-serif; font-weight: 900;
    font-size: 26px; letter-spacing: 1px;
    color: var(--ink); text-transform: uppercase;
  }
  .brand__since {
    margin-top: 14px;
    font-family: "Roboto", sans-serif; font-weight: 700;
    font-size: 17px; color: var(--ink); text-transform: uppercase;
  }
  .origin {
    position: absolute; left: 0; right: 0; top: 960px;
    text-align: center;
    font-family: "Roboto", sans-serif; font-weight: 700;
    font-size: 20px; line-height: 1.35;
    color: var(--ink-soft); text-transform: uppercase;
  }
  .origin .from { font-size: 16px; }
</style>
</head>
<body>
  <div class="bag">
    <aside class="bag__side">
      <p class="mission">We aim to be a coffee company for the people. The people who have an appreciation and love for family, community and who never forget where they came from. Our coffee was born out of West Louisville, KY… a place like many others where the hearts, the minds and the wills are strong. We hope you enjoy each and every cup. Peace &amp; Blessings.</p>
    </aside>
    <section class="bag__front">
      <div class="stitch"></div>
      <svg class="ribbon" viewBox="0 0 230 420" aria-hidden="true">
        <polygon points="0,0 230,0 230,420 115,340 0,420" fill="var(--ink)"/>
      </svg>
      <div class="ribbon__label">
        <span class="small">Perfectly</span>
        <span class="big">Roast</span>
      </div>
      <div class="brand">
        <span class="brand__dot"></span>
        <h1 class="brand__name">Brindle Oak<br>Coffee</h1>
        <p class="brand__tag">Premium Quality</p>
        <p class="brand__since">Since 1900</p>
      </div>
      <p class="origin">Another greatness <span class="from">from</span><br>West Louisville, KY</p>
    </section>
  </div>
</body>
</html>
```